Business Card Design Project

I need some business cards with the logo you did for us (attached)
I am looking for a coulourful yet serious business card

We do market research
on the back I want the logo

on the front my name : Corinne Valdessac
position : Manager
address : Brume Analytica Sarl - 27 Rue des tanneurs
1847 Glarency - Switzerland
corinne.valdessac@brumeanalytica.ch
Tel : +4122 934 07 58
Mob France :+33 671 42 8356
Mob Italy +39 347 520 8163

The tree of the logo could also be used alone

THE BACKGROUND COLOR ON THE FRONT HAS TO BE WHITE, ON THE BACK YU CAN TRY OHER COLOUR BUT HOMOGENEOUS (NOT EXPENSIVE TO PRINT)

Target Market(s)

multinational companies or other market research companies

Industry/Entity Type

Market Research

Requirements
Must have
• logo on the back
and all the info above

```html
<!DOCTYPE html>
<html lang="en">
<head>
<meta charset="utf-8">
<title>Brume Analytica – Business Card</title>
<link rel="stylesheet" href="https://fonts.googleapis.com/css2?family=Questrial&display=swap">
<style>
  :root {
    --brand-red: #b0292f;
    --brand-pink: #d8336a;
    --ink: #3a3a3a;
    --paper: #ffffff;
    --backdrop: #e4e7ea;
  }
  * { box-sizing: border-box; margin: 0; padding: 0; }
  html, body {
    width: 1200px;
    height: 960px;
    overflow: hidden;
  }
  body {
    background: var(--backdrop);
    font-family: "Questrial", sans-serif;
    color: var(--ink);
    position: relative;
  }
  .card {
    position: absolute;
    left: 280px;
    width: 640px;
    height: 414px;
    box-shadow: 0 6px 18px rgba(0,0,0,0.18);
  }

  /* Back side */
  .card-back {
    top: 40px;
    background: var(--brand-red);
    display: flex;
    align-items: center;
    justify-content: center;
  }
  .brand {
    display: flex;
    align-items: center;
    white-space: nowrap;
  }
  .brand-dot {
    flex: none;
    border-radius: 50%;
  }
  .card-back .brand { gap: 18px; }
  .card-back .brand-dot {
    width: 30px;
    height: 30px;
    background: var(--paper);
  }
  .card-back .brand-name {
    color: var(--paper);
    font-size: 52px;
    letter-spacing: 0.5px;
    line-height: 1;
  }

  /* Front side */
  .card-front {
    top: 506px;
    background: var(--paper);
  }
  .identity {
    position: absolute;
    left: 34px;
    top: 74px;
    padding-left: 20px;
    border-left: 7px solid var(--brand-red);
  }
  .person-name {
    font-size: 25px;
    letter-spacing: 0.8px;
    line-height: 1.1;
  }
  .person-role {
    font-size: 21px;
    letter-spacing: 0.6px;
    line-height: 1.15;
  }
  .address {
    position: absolute;
    left: 61px;
    top: 200px;
    font-style: normal;
    font-size: 16px;
    line-height: 1.3;
  }
  .card-front .brand {
    position: absolute;
    right: 40px;
    top: 96px;
    gap: 12px;
  }
  .card-front .brand-dot {
    width: 20px;
    height: 20px;
    background: var(--brand-pink);
  }
  .card-front .brand-name {
    color: var(--brand-pink);
    font-size: 34px;
    line-height: 1;
  }
  .contacts {
    position: absolute;
    left: 336px;
    top: 238px;
    list-style: none;
    font-size: 14.5px;
    line-height: 1.35;
    white-space: nowrap;
  }
  .contacts li {
    display: flex;
    align-items: center;
    gap: 10px;
  }
  .contacts svg {
    width: 12px;
    height: 12px;
    flex: none;
    fill: var(--brand-red);
  }
</style>
</head>
<body>
  <section class="card card-back" aria-label="Card back">
    <div class="brand">
      <span class="brand-dot" aria-hidden="true"></span>
      <span class="brand-name">brume analytica</span>
    </div>
  </section>

  <section class="card card-front" aria-label="Card front">
    <div class="identity">
      <p class="person-name">Corinne Valdessac</p>
      <p class="person-role">Manager</p>
    </div>
    <address class="address">
      Brume Analytica Sarl<br>
      27 Rue des tanneurs<br>
      1847 Glarency - Switzerland
    </address>
    <div class="brand">
      <span class="brand-dot" aria-hidden="true"></span>
      <span class="brand-name">brume analytica</span>
    </div>
    <ul class="contacts">
      <li>
        <svg viewBox="0 0 12 12" aria-hidden="true"><path d="M0 2h12v8H0z"/><path d="M1 3l5 3.5L11 3" fill="none" stroke="#fff" stroke-width="1"/></svg>
        corinne.valdessac@brumeanalytica.ch
      </li>
      <li>
        <svg viewBox="0 0 12 12" aria-hidden="true"><path d="M2.5 1l2 2.5-1.2 1.3a7 7 0 0 0 3.9 3.9L8.5 7.5l2.5 2-1.2 1.8C5 11 1 7 .7 2.2z"/></svg>
        +4122 934 07 58
      </li>
      <li>
        <svg viewBox="0 0 12 12" aria-hidden="true"><rect x="3" y="0.5" width="6" height="11" rx="1"/><rect x="4" y="2" width="4" height="6" fill="#fff"/></svg>
        +33 671 42 8356 (France)
      </li>
      <li>
        <svg viewBox="0 0 12 12" aria-hidden="true"><rect x="3" y="0.5" width="6" height="11" rx="1"/><rect x="4" y="2" width="4" height="6" fill="#fff"/></svg>
        +39 347 520 8163 (Italy)
      </li>
    </ul>
  </section>
</body>
</html>
```